Business Card Design Project

We need a simple business card design that uses our current logo.
We need to have the current logo put into a high res format.
We need to have 1 card made with contact information.
We will supply the information for the 4 employees.
Industry/Entity Type
Business
Requirements
Must have
- The contact information is as follows:
Mark Dellweather
Producer/CEO
c. 949-555-0147
f. 650-555-0193
markd@lanternbay.example
Al Vostrand, CFO
c. 949-555-0162
f. 650-555-0193
alv@lanternbay.example
Peter Malvane, PR
c. 267-555-0128
f. 650-555-0193
pmalvane@lanternbay.example
Tim Garrowby, Producer
c. 949-555-0184
f. 650-555-0193
timg@lanternbay.example
The address for all cards is:
318 W Calle Norvento #2715, San Clemente, CA 92681

```html
<!DOCTYPE html>
<html lang="en">
<head>
<meta charset="utf-8">
<title>Lantern Bay Media – Business Card</title>
<link rel="stylesheet" href="https://fonts.googleapis.com/css2?family=Arimo:wght@400;700&display=swap">
<style>
  :root {
    --magenta-light: #c22d80;
    --magenta-dark: #8f1659;
    --card-white: #ffffff;
    --rim-grey: #c9c9cf;
    --ink: #111111;
    --address-white: #ffffff;
  }
  * { margin: 0; padding: 0; box-sizing: border-box; }
  html, body {
    width: 1200px;
    height: 678px;
    overflow: hidden;
    background: #ffffff;
  }
  .business-card {
    position: relative;
    width: 1200px;
    height: 678px;
    overflow: hidden;
    background: linear-gradient(160deg, var(--magenta-light) 0%, var(--magenta-dark) 100%);
    font-family: "Arimo", Arial, sans-serif;
  }
  .card-swoosh {
    position: absolute;
    inset: 0;
    width: 1200px;
    height: 678px;
  }
  .brand-name {
    position: absolute;
    top: 102px;
    left: 0;
    width: 1030px;
    text-align: center;
    font-weight: 700;
    font-size: 58px;
    line-height: 72px;
    color: var(--ink);
  }
  .contact-block {
    position: absolute;
    top: 234px;
    left: 0;
    width: 1030px;
    text-align: center;
    color: var(--ink);
    font-size: 27px;
    line-height: 40px;
  }
  .address-line {
    position: absolute;
    top: 616px;
    left: 0;
    width: 1166px;
    text-align: center;
    color: var(--address-white);
    font-size: 29px;
    line-height: 36px;
  }
</style>
</head>
<body>
  <div class="business-card">
    <svg class="card-swoosh" viewBox="0 0 1200 678" aria-hidden="true">
      <ellipse cx="466" cy="134" rx="616" ry="446" fill="var(--rim-grey)"/>
      <ellipse cx="464" cy="130" rx="612" ry="440" fill="var(--card-white)"/>
    </svg>

    <p class="brand-name">Lantern Bay Media</p>

    <div class="contact-block">
      <p class="contact-name">Mark Dellweather</p>
      <p class="contact-title">Producer/CEO</p>
      <p class="contact-cell">c. 949-555-0147</p>
      <p class="contact-fax">f. 650-555-0193</p>
      <p class="contact-email">markd@lanternbay.example</p>
    </div>

    <p class="address-line">318 W Calle Norvento #2715, San Clemente, CA 92681</p>
  </div>
</body>
</html>
```